This is not a sticker but a fridge magnet for ridge plumbing.

The dimensions of magnet/sticker are lenght 100mmX Height 70mm. or vice versa

I want the magnet to look clean and not messy
The magnet is to capture the audience straight away.

I would like the heading to be "Everyday Low Cost Plumbing 24/7" or something that catches the audience. thats your choice ;-)

Also: "Present this magnet and receive 15% discount"
The 15% discount needs to stand out

The tick boxes can be small as I dont want the magnet looking too busy.

I would like tick boxes for the following:

Same Day Service/emergency service
Blocked drains
Hot Water
Burst Pipe, Leaking Taps & Toilets
Gas Installations
Leak Detection
Pipe Relining

PH 1300 482 957 or book online

down the bottom of magnet: ridgeplumbingco.com.au

also down the bottom small text: t&c see our website.
bottom right corner Lic 583914K

also have facebook icon youtube icon instagram icon and google plus icon.these icons can be small not big. Added Monday, March 7, 2016

Also this needs to be high definition Added Monday, March 7, 2016

house holds as it will be on their fridge

Plumbing

• 15% discount
• ph number
• lic. number
• Basic yet attractive clean

```html
<!DOCTYPE html>
<html lang="en">
<head>
<meta charset="utf-8">
<title>Ridge Plumbing – Fridge Magnet</title>
<link href="https://fonts.googleapis.com/css2?family=Oswald:wght@600&family=Lato:wght@700&family=Arimo:ital,wght@0,700;1,700&display=swap" rel="stylesheet">
<style>
  :root {
    --page-bg: #ffffff;
    --card: #ffffff;
    --brand-blue: #2f4f9a;
    --sky: #58a6d6;
    --teal: #1e8fb0;
    --light-wave: #6aa9e0;
    --ink: #000000;
    --white: #ffffff;
    --badge-red: #d0463a;
    --icon-grey: #dbe7ee;
  }
  * { margin: 0; padding: 0; box-sizing: border-box; }
  html, body { width: 1200px; height: 1000px; overflow: hidden; background: var(--page-bg); }
  .canvas { position: relative; width: 1200px; height: 1000px; }
  .artwork { position: absolute; inset: 0; }
  .abs { position: absolute; }

  .brand-name {
    left: 310px; width: 575px; top: 258px; text-align: center;
    font-family: "Arimo", Arial, sans-serif; font-weight: 700;
    font-size: 50px; line-height: 1; color: var(--brand-blue);
  }
  .tagline {
    left: 310px; width: 575px; top: 313px; text-align: center;
    font-family: "Arimo", Arial, sans-serif; font-weight: 700;
    font-size: 22px; line-height: 1; color: var(--sky);
  }
  .headline {
    left: 310px; width: 575px; top: 356px; text-align: center;
    font-family: "Oswald", "Arial Narrow", sans-serif; font-weight: 600;
    font-size: 34px; line-height: 1.2; color: var(--ink); letter-spacing: 0.3px;
  }
  .service-list {
    left: 376px; top: 434px; list-style: none;
    font-family: "Arimo", Arial, sans-serif; font-weight: 700; font-size: 21px; color: var(--white);
  }
  .service-list li { display: flex; align-items: center; height: 33.6px; }
  .service-list svg { width: 14px; height: 18px; margin-right: 10px; flex: none; }

  .offer {
    left: 662px; width: 200px; top: 604px; text-align: center; color: var(--white);
    font-family: "Arimo", Arial, sans-serif; font-weight: 700;
  }
  .offer-lead { font-style: italic; font-size: 15px; line-height: 14px; }
  .offer-value { font-size: 54px; line-height: 52px; margin-top: 2px; }
  .offer-word { font-size: 22px; line-height: 20px; }

  .phone-line {
    left: 422px; top: 800px;
    font-family: "Arimo", Arial, sans-serif; font-weight: 700; font-size: 23px; color: var(--teal); letter-spacing: 0.3px;
  }
  .find-us {
    left: 454px; top: 846px;
    font-family: "Arimo", Arial, sans-serif; font-weight: 700; font-size: 20px; color: var(--white); letter-spacing: 1.5px;
  }
  .web, .licence {
    top: 882px; font-family: "Lato", sans-serif; font-weight: 700; font-size: 24px; color: var(--white);
  }
  .web { left: 364px; }
  .licence { left: 675px; }
</style>
</head>
<body>
<main class="canvas">
  <svg class="artwork" width="1200" height="1000" viewBox="0 0 1200 1000" aria-hidden="true">
    <defs>
      <clipPath id="card-clip"><rect x="310" y="104" width="575" height="821"/></clipPath>
    </defs>
    <rect class="card" x="310" y="104" width="575" height="821" fill="var(--card)"/>

    <circle cx="597" cy="192" r="50" fill="var(--brand-blue)"/>

    <g clip-path="url(#card-clip)">
      <path d="M300 700 Q500 708 650 726 T895 708 L895 740 Q700 756 300 722 Z" fill="var(--light-wave)"/>
      <path d="M300 738 Q500 732 640 758 T895 742 L895 930 L300 930 Z" fill="var(--teal)"/>
      <path d="M300 752 Q500 746 640 772 T895 756" fill="none" stroke="var(--white)" stroke-width="5"/>
    </g>

    <rect x="352" y="414" width="496" height="274" rx="14" fill="var(--ink)"/>
    <rect x="361" y="424" width="472" height="254" fill="none" stroke="var(--teal)" stroke-width="6"/>
    <g fill="none" stroke="var(--white)" stroke-width="7">
      <polyline points="361,460 361,424 398,424"/>
      <polyline points="800,424 833,424 833,460"/>
      <polyline points="361,640 361,678 398,678"/>
      <line x1="833" y1="455" x2="833" y2="465" stroke-width="10"/>
      <line x1="356" y1="460" x2="366" y2="460"/>
      <line x1="356" y1="640" x2="366" y2="640"/>
      <line x1="398" y1="673" x2="398" y2="683"/>
      <line x1="398" y1="419" x2="398" y2="429"/>
      <line x1="800" y1="419" x2="800" y2="429"/>
    </g>

    <g transform="translate(766 672)">
      <polygon fill="var(--ink)" points="100,0 85.3,11.2 96.6,25.9 79.5,32.9 86.6,50 68.2,52.4 70.7,70.7 52.4,68.2 50,86.6 32.9,79.5 25.9,96.6 11.2,85.3 0,100 -11.2,85.3 -25.9,96.6 -32.9,79.5 -50,86.6 -52.4,68.2 -70.7,70.7 -68.2,52.4 -86.6,50 -79.5,32.9 -96.6,25.9 -85.3,11.2 -100,0 -85.3,-11.2 -96.6,-25.9 -79.5,-32.9 -86.6,-50 -68.2,-52.4 -70.7,-70.7 -52.4,-68.2 -50,-86.6 -32.9,-79.5 -25.9,-96.6 -11.2,-85.3 0,-100 11.2,-85.3 25.9,-96.6 32.9,-79.5 50,-86.6 52.4,-68.2 70.7,-70.7 68.2,-52.4 86.6,-50 79.5,-32.9 96.6,-25.9 85.3,-11.2"/>
    </g>
    <g transform="translate(762 668)">
      <polygon fill="var(--badge-red)" stroke="var(--white)" stroke-width="1.5" points="100,0 85.3,11.2 96.6,25.9 79.5,32.9 86.6,50 68.2,52.4 70.7,70.7 52.4,68.2 50,86.6 32.9,79.5 25.9,96.6 11.2,85.3 0,100 -11.2,85.3 -25.9,96.6 -32.9,79.5 -50,86.6 -52.4,68.2 -70.7,70.7 -68.2,52.4 -86.6,50 -79.5,32.9 -96.6,25.9 -85.3,11.2 -100,0 -85.3,-11.2 -96.6,-25.9 -79.5,-32.9 -86.6,-50 -68.2,-52.4 -70.7,-70.7 -52.4,-68.2 -50,-86.6 -32.9,-79.5 -25.9,-96.6 -11.2,-85.3 0,-100 11.2,-85.3 25.9,-96.6 32.9,-79.5 50,-86.6 52.4,-68.2 70.7,-70.7 68.2,-52.4 86.6,-50 79.5,-32.9 96.6,-25.9 85.3,-11.2"/>
    </g>

    <rect x="380" y="797" width="474" height="36" rx="18" fill="var(--white)"/>
    <g class="phone-icon" fill="var(--white)">
      <path d="M352 803 Q385 782 418 803 L416 813 L404 811 L402 803 Q385 797 368 803 L366 811 L354 813 Z"/>
      <path d="M368 812 L402 812 L414 836 L356 836 Z"/>
      <circle cx="385" cy="823" r="9" fill="var(--teal)"/>
      <circle cx="385" cy="823" r="4"/>
    </g>

    <g fill="var(--icon-grey)">
      <rect x="590" y="846" width="28" height="22" rx="4"/>
      <rect x="636" y="845" width="24" height="24" rx="4"/>
      <circle cx="686" cy="857" r="12"/>
      <rect x="716" y="845" width="25" height="25" rx="2"/>
    </g>
  </svg>

  <div class="abs brand-name">Ridge Plumbing</div>
  <div class="abs tagline">Honest Work, Every Time</div>
  <h1 class="abs headline">Everyday Low Cost Plumbing 24/7</h1>

  <ul class="abs service-list">
    <li><svg viewBox="0 0 14 18"><path d="M7 1 Q13 9 12 12 A5 5 0 0 1 2 12 Q1 9 7 1 Z" fill="var(--teal)"/></svg>Same Day Service/emergency service</li>
    <li><svg viewBox="0 0 14 18"><path d="M7 1 Q13 9 12 12 A5 5 0 0 1 2 12 Q1 9 7 1 Z" fill="var(--teal)"/></svg>Blocked drains</li>
    <li><svg viewBox="0 0 14 18"><path d="M7 1 Q13 9 12 12 A5 5 0 0 1 2 12 Q1 9 7 1 Z" fill="var(--teal)"/></svg>Hot Water</li>
    <li><svg viewBox="0 0 14 18"><path d="M7 1 Q13 9 12 12 A5 5 0 0 1 2 12 Q1 9 7 1 Z" fill="var(--teal)"/></svg>Burst Pipe, Leaking Taps &amp; Toilets</li>
    <li><svg viewBox="0 0 14 18"><path d="M7 1 Q13 9 12 12 A5 5 0 0 1 2 12 Q1 9 7 1 Z" fill="var(--teal)"/></svg>Gas Installations</li>
    <li><svg viewBox="0 0 14 18"><path d="M7 1 Q13 9 12 12 A5 5 0 0 1 2 12 Q1 9 7 1 Z" fill="var(--teal)"/></svg>Leak Detection</li>
    <li><svg viewBox="0 0 14 18"><path d="M7 1 Q13 9 12 12 A5 5 0 0 1 2 12 Q1 9 7 1 Z" fill="var(--teal)"/></svg>Pipe Relining</li>
  </ul>

  <div class="abs offer">
    <p class="offer-lead">Present this<br>magnet and<br>receive</p>
    <p class="offer-value">15%</p>
    <p class="offer-word">discount</p>
  </div>

  <p class="abs phone-line">PH 1300 482 957 or book online</p>
  <p class="abs find-us">Find Us at</p>
  <p class="abs web">ridgeplumbingco.com.au</p>
  <p class="abs licence">Lic 583914K</p>
</main>
</body>
</html>
```